wedding package brochure

We want to freshen the look for our wedding packages. Attached is a link to the current content
http://www.tarwinheadslinks.com.au/weddings/THL-Wedding-Package-2012-2013.pdf
We would like the logo (the dolphins) included and it needs to showcase the beachside location and give a classy wedding feel. I have a style guide available if required.

Industry/Entity Type

Wedding

```html
<!DOCTYPE html>
<html lang="en">
<head>
<meta charset="utf-8">
<title>Tarwin Heads Links – Dinner &amp; Buffet Menus</title>
<link rel="stylesheet" href="https://fonts.googleapis.com/css2?family=Great+Vibes&family=Tinos&display=swap">
<style>
  :root {
    --green-deep: #3d8a33;
    --green-mid: #5fa848;
    --green-light: #8cc46a;
    --title-yellow: #f6f200;
    --body-white: #ffffff;
    --frame: #c9d9bd;
  }
  html, body {
    margin: 0;
    padding: 0;
    overflow: hidden;
    background: #ffffff;
  }
  .menu-page {
    position: relative;
    width: 848px;
    height: 1200px;
    overflow: hidden;
    background: radial-gradient(ellipse 70% 55% at 50% 50%, var(--green-light) 0%, var(--green-mid) 50%, var(--green-deep) 100%);
  }
  .side-ornament {
    position: absolute;
    top: 0;
    width: 170px;
    height: 1200px;
  }
  .side-ornament--left {
    left: 0;
    background: linear-gradient(90deg, rgba(140, 196, 106, 0.22), rgba(140, 196, 106, 0));
  }
  .side-ornament--right {
    right: 0;
    background: linear-gradient(270deg, rgba(140, 196, 106, 0.22), rgba(140, 196, 106, 0));
  }
  .menu-title {
    position: absolute;
    left: 0;
    width: 848px;
    margin: 0;
    text-align: center;
    font-family: "Great Vibes", cursive;
    font-weight: 400;
    color: var(--title-yellow);
    line-height: 70px;
  }
  .menu-title--dinner {
    top: 40px;
    font-size: 60px;
  }
  .menu-title--buffet {
    top: 589px;
    font-size: 62px;
  }
  .menu-items {
    position: absolute;
    left: 0;
    width: 848px;
    margin: 0;
    text-align: center;
    font-family: "Tinos", serif;
    font-size: 19px;
    line-height: 30px;
    color: var(--body-white);
    white-space: nowrap;
  }
  .menu-items--dinner { top: 179px; }
  .menu-items--buffet { top: 668px; }
  .photo-frame {
    position: absolute;
    box-sizing: border-box;
    border: 6px solid var(--frame);
  }
  .photo-frame--flowers {
    left: 207px;
    top: 398px;
    width: 448px;
    height: 164px;
    background: linear-gradient(100deg, #6b3a4e 0%, #c66a9e 25%, #e4a8d2 45%, #b87ab8 65%, #e8d8ea 85%, #c45a9a 100%);
  }
  .photo-frame--glasses {
    left: 231px;
    top: 974px;
    width: 403px;
    height: 187px;
    background: linear-gradient(180deg, #5a3a2a 0%, #9a7a6a 30%, #c8c0c0 55%, #7a5a5a 80%, #6a2a5a 100%);
  }
</style>
</head>
<body>
<main class="menu-page">
  <div class="side-ornament side-ornament--left" role="img" aria-label="Faint scrolling leaf ornament along the left edge"></div>
  <div class="side-ornament side-ornament--right" role="img" aria-label="Faint scrolling leaf ornament along the right edge"></div>

  <h1 class="menu-title menu-title--dinner">The 3 Course Dinner<br>Menu B</h1>
  <p class="menu-items menu-items--dinner">Sauté of Garlic King Prawns on Rice Pilaf Sauté of Garlic King<br>PrawnsThai Marinated Beef on Oriental Salad with Sesame D Thai<br>Marinated Beef ressing Tempura Dipped Chicken Strips w Chilli<br>Plum on Jasm Tempura Dipped Chicken Strips ine Rice<br>Anti----Pasta Prawn Pasta Prawn Pasta Prawn wrapped w Egg-<br>plant, Pesto and Semi Dried Tomato Mushroom and Asparagus Vol<br>Au Vent set on a bed of Mushroom and Asparagus Green Salad</p>

  <div class="photo-frame photo-frame--flowers" role="img" aria-label="Photo of a pink and purple floral table arrangement"></div>

  <h2 class="menu-title menu-title--buffet">Buffet Selection Menu One</h2>
  <p class="menu-items menu-items--buffet">Atlantic Salmon Fillets w Tarragon &amp; Vine Le Seared Atlantic<br>Salmon aves Pepper Crust Eye Fillet Medallions Pepper Crust Eye<br>FilletMedallions Medallions on Garlic Mash<br>Whole Local King Prawns Grilled w Sweet Soy &amp; Ginger Whole<br>Local King Prawns on Fried Noodles Rump Steak and Tomato<br>Sausages Rump SteakCrispy Skin Chicken Pieces in Lime and<br>Chilli Crispy Skin Chicken PiecesSweet Potato Lasagne w English<br>Spinach, Roasted Cap Sweet Potato Lasagne sicum and Ricotta<br>Barbequed Fried Rice w Egg, Onion, Bacon and Mushro Barbqued<br>Fried Rice om Jacket Roasted Potatoes w Sour Cream and Chives</p>

  <div class="photo-frame photo-frame--glasses" role="img" aria-label="Photo of stacked champagne coupe glasses"></div>
</main>
</body>
</html>
```